whitening gel shopping website design

Hello:
We would like to create a whitening gel selling website. It will be very close to Glowbrite, but different designs. https://us.glowbriteorals.example/

What is your organization or website name?
Velvet Beaming

Industry: health and beauty
Target user: ladies between 16 to 40, please make the website friendly and lovely

website pages: main website, shop products, enrolled monthly plans, about us, contact us, policy, customer login log out, shopping cart, customer dashboard.

Website main page contains:
1. one slide show that shows advertisements.
2. show current promo codes
3.show a brief overview about our history
4. show a brief overview about the product introduction
5. show a brief overview of our monthly enrolled product plan
6. have an area to show blogs and posts (please take a look at Glowbrite home page)
7. buttons for customer to login, sign up, visit home, about us, policy, returns, subscription etc.

Note: for the contest, please finish the website main page and the product page only, now we don’t have any logo, test or images, please use yours for now.

```html
<!DOCTYPE html>
<html lang="en">
<head>
<meta charset="utf-8">
<title>Velvet Beaming – Home</title>
<link rel="stylesheet" href="https://fonts.googleapis.com/css2?family=Roboto:wght@300;400;500;700&display=swap">
<style>
:root{
  --ink:#2b2b2b;
  --text:#4a4a4a;
  --muted:#7a7a7a;
  --line:#dcdcdc;
  --pink:#f5b9d0;
  --pink-deep:#e98fb0;
  --dark:#1e1e1e;
  --white:#ffffff;
  --footer-bar:#1f1f1f;
}
*{box-sizing:border-box;margin:0;padding:0}
html,body{width:1200px;height:3598px;overflow:hidden;background:var(--white)}
body{position:relative;font-family:"Roboto",Arial,sans-serif;color:var(--text);font-weight:300}
.abs{position:absolute}
a{color:inherit;text-decoration:none}
.icon{stroke:var(--text);fill:none;stroke-width:1.4;stroke-linecap:round;stroke-linejoin:round}

/* header */
.topbar{left:0;top:0;width:1200px;height:75px;border-bottom:1px solid var(--line)}
.phone{left:38px;top:21px;font-size:14px;display:flex;align-items:center;gap:9px}
.brand{font-size:19px;color:var(--ink);font-weight:400;display:flex;align-items:center;gap:6px}
.brand b{font-weight:700}
.brand .dot{width:9px;height:9px;border-radius:50%;background:var(--pink-deep)}
.header-brand{left:0;width:1200px;top:30px;justify-content:center}
.tools{right:40px;top:18px;display:flex;gap:22px;align-items:center;font-size:11px}
.mainnav{left:0;top:75px;width:1200px;height:55px;border-bottom:1px solid var(--line);display:flex;justify-content:center;align-items:center;gap:30px;font-size:14px;color:var(--ink)}

/* perks */
.perks{left:0;top:130px;width:1200px;height:82px;display:flex;justify-content:center;align-items:center}
.perk{display:flex;align-items:center;gap:42px;padding:0 50px;height:50px}
.perk + .perk{border-left:1px solid var(--line)}
.perk-text{text-align:center}
.perk-text strong{display:block;font-size:12.5px;font-weight:500;color:var(--ink)}
.perk-text span{font-size:11px;color:var(--muted)}
.perk-text u{font-size:11px;color:var(--muted)}

/* photo fills */
.photo{position:absolute}
.hero-photo{left:0;top:212px;width:1200px;height:563px;background:linear-gradient(90deg,#f3f1ec 0%,#efe8df 45%,#d9c0ac 62%,#f1ece6 85%,#fafafa 100%)}
.photo-a{left:600px;top:775px;width:600px;height:408px;background:linear-gradient(120deg,#cfd3d6,#e9ecec 50%,#c8ab92 80%,#eef0f1)}
.photo-b{left:0;top:1183px;width:602px;height:407px;background:radial-gradient(ellipse at 50% 55%,#f4efe5 0%,#e8b3ae 30%,#c98a72 60%,#b97a60 100%)}
.photo-c{left:600px;top:1590px;width:600px;height:407px;background:linear-gradient(135deg,#f2f2f2,#e6d3c5 40%,#3d86cf 70%,#eeeeee)}
.photo-d{left:0;top:1997px;width:602px;height:407px;background:linear-gradient(180deg,#e3e6ea,#c9ced4 70%,#b8917c)}

/* text blocks */
.feature h2{font-size:24px;font-weight:300;color:var(--ink);line-height:1.2}
.feature h3{font-size:29px;font-weight:700;color:#3a3a3a;line-height:1.2}
.feature p{margin-top:22px;font-size:13.5px;line-height:17px;color:var(--muted);width:345px}
.btn{display:inline-flex;align-items:center;justify-content:center;width:162px;height:46px;font-size:14px;background:var(--dark);color:var(--white);margin-top:24px;margin-left:2px}
.btn.pink{background:var(--pink);color:#333}
.hero h2{font-size:50px;font-weight:300;line-height:1.2}
.hero h3{font-size:52px;font-weight:700;line-height:1.15}
.hero p{margin-top:22px;font-size:14px;color:#666}

/* newsletter */
.news{left:0;top:2478px;width:1200px;height:112px;border-top:1px solid var(--line);border-bottom:1px solid var(--line)}
.news h2{position:absolute;left:120px;top:38px;font-size:28px;font-weight:300;color:var(--ink)}
.news h2 b{font-weight:700}
.news .field{position:absolute;left:521px;top:30px;width:393px;height:47px;border:1px solid #cfcfcf;font-size:13.5px;font-style:italic;color:#999;padding:15px 22px}
.news .go{position:absolute;left:917px;top:30px;width:163px;height:47px;background:var(--dark);color:var(--white);font-size:14px;display:flex;align-items:center;justify-content:center}

/* blog */
.blog-intro{left:45px;top:2650px}
.blog-intro p{width:350px}
.post h4{font-size:19px;font-weight:700;color:#3a3a3a}
.post time{display:block;font-size:13.5px;color:var(--muted);margin-top:10px}
.post p{font-size:13.5px;line-height:17px;color:var(--muted);width:300px}
.more{display:inline-flex;align-items:center;gap:5px;font-size:13.5px;color:#444;text-decoration:underline;margin-top:25px}
.post-photo-1{left:409px;top:2660px;width:332px;height:332px;background:linear-gradient(135deg,#f1e3da,#d9a58f 40%,#6a4fd6 65%,#2f7bc7 85%,#eaeaea)}
.post-photo-2{left:771px;top:2660px;width:113px;height:113px;background:linear-gradient(135deg,#eef1f3,#d7d3cf)}
.post-photo-3{left:771px;top:2953px;width:113px;height:113px;background:linear-gradient(135deg,#e2a39a,#f3ede4 50%,#d98b86)}

/* footer */
.footer{left:0;top:3250px;width:1200px;height:308px;border-top:1px solid var(--line)}
.fcol{position:absolute;top:75px;font-size:14px;color:#444}
.fcol h5{font-size:14px;font-weight:500;color:var(--ink);margin-bottom:32px;margin-top:-50px}
.fcol li{list-style:none;height:29px}
.cards{position:absolute;left:970px;top:183px;display:flex;gap:8px}
.card{width:42px;height:30px;border-radius:3px;color:#fff;font-size:8.5px;font-weight:500;display:flex;align-items:center;justify-content:center}
.bottom{left:0;top:3558px;width:1200px;height:40px;background:var(--footer-bar);color:#eee;font-size:13.5px}
.bottom .copy{position:absolute;left:39px;top:12px}
.social{position:absolute;right:39px;top:8px;display:flex;gap:8px}
.social span{height:24px;border:1px solid #bbb;font-size:9px;padding:0 5px;display:flex;align-items:center}
</style>
</head>
<body>

<header class="abs topbar">
  <div class="abs phone">
    <svg width="16" height="16" viewBox="0 0 16 16" class="icon"><path d="M3 1.5l3 3-1.7 1.8a9 9 0 0 0 5.4 5.4L11.5 10l3 3-2 2C6.5 15 1 9.5 1 3.5z"/></svg>
    012 555 0147
  </div>
  <a class="abs brand header-brand">Velvet<b>Beaming</b></a>
  <div class="abs tools">
    <svg width="18" height="18" viewBox="0 0 18 18" class="icon"><circle cx="7.5" cy="7.5" r="6"/><path d="M12 12l5 5"/></svg>
    <svg width="18" height="18" viewBox="0 0 18 18" class="icon"><circle cx="9" cy="5.5" r="4"/><path d="M2 17c0-4 3-6 7-6s7 2 7 6z"/></svg>
    <span style="display:flex;gap:4px;align-items:flex-start"><svg width="20" height="18" viewBox="0 0 20 18" class="icon"><path d="M1 1h3l2.5 11h10L19 4H5"/><circle cx="8" cy="15.5" r="1.4"/><circle cx="15" cy="15.5" r="1.4"/></svg>0</span>
  </div>
</header>

<nav class="abs mainnav">
  <a>Home</a><a>Shop Products</a><a>Enrooled Monthly Plans</a><a>About us</a><a>Contact us</a>
</nav>

<section class="abs perks">
  <div class="perk">
    <svg width="28" height="20" viewBox="0 0 28 20" class="icon"><path d="M9 3h12v11H9zM21 7h4l2 3v4h-6"/><circle cx="12" cy="16" r="2"/><circle cx="23" cy="16" r="2"/><path d="M2 7h5M3 10h4"/></svg>
    <div class="perk-text"><strong>Free Shipping Worldwide</strong><u>Click here for more info</u></div>
  </div>
  <div class="perk">
    <svg width="22" height="22" viewBox="0 0 22 22" class="icon"><path d="M4 12V10a7 7 0 0 1 14 0v2"/><rect x="3" y="11" width="3" height="6" rx="1"/><rect x="16" y="11" width="3" height="6" rx="1"/><path d="M17 17c0 2-3 3-6 3"/></svg>
    <div class="perk-text"><strong>Customer Service</strong><span>24/7 customer support service</span></div>
  </div>
  <div class="perk">
    <svg width="24" height="22" viewBox="0 0 24 22" class="icon"><path d="M3 4h14v10H3z"/><path d="M14 17h7M18 14l3 3-3 3"/></svg>
    <div class="perk-text"><strong>Return policy</strong><span>within 3 days of the date of purchase</span></div>
  </div>
</section>

<div class="photo hero-photo" role="img" aria-label="Photo of a smiling woman resting her chin on her hand on a white sofa"></div>
<section class="abs feature hero" style="left:119px;top:360px;color:#444">
  <h2>What your</h2>
  <h3>Smile needs?</h3>
  <p>Our range of products is designed for every step of your oral hygiene routine, using all natural ingredients to ensure there's no pain or sensitivity.</p>
  <a class="btn pink">SHOP NOW</a>
</section>

<section class="abs feature" style="left:119px;top:875px">
  <h2>Get Promotion</h2>
  <h3>Save Upto 30% Off</h3>
  <p>Lorem Ipsum is simply dummy text of the printing and typesetting industry. Lorem Ipsum has been the industry's standard dummy text ever since the 1500s</p>
  <a class="btn">SHOP NOW</a>
</section>
<div class="photo photo-a" role="img" aria-label="Photo of a man in a bathrobe holding a blue whitening tray in front of a mirror"></div>

<div class="photo photo-b" role="img" aria-label="Close-up photo of smiling lips showing teeth before and after whitening"></div>
<section class="abs feature" style="left:697px;top:1280px">
  <h2>About us</h2>
  <h3>Velvet Beaming History</h3>
  <p>Lorem Ipsum is simply dummy text of the printing and typesetting industry. Lorem Ipsum has been the industry's standard dummy text ever since the 1500s</p>
  <a class="btn">READ MORE</a>
</section>

<section class="abs feature" style="left:119px;top:1693px">
  <h2>Wide range of</h2>
  <h3>Our Products</h3>
  <p>Our range of products is designed for every step of your oral hygiene routine, using all natural ingredients to ensure there's no pain or sensitivity.</p>
  <a class="btn">VIEW PRODUCTS</a>
</section>
<div class="photo photo-c" role="img" aria-label="Photo of a smiling woman holding a blue LED whitening mouthpiece"></div>

<div class="photo photo-d" role="img" aria-label="Photo of a woman looking up at many drawn question marks"></div>
<section class="abs feature" style="left:697px;top:2110px">
  <h2>Monthly enrolled</h2>
  <h3>Product Plan</h3>
  <p>Have all of your favourite products delivered to your front door at a frequency of your choice with our Product Plans.</p>
  <a class="btn">Choose your Plan</a>
</section>

<section class="abs news">
  <h2>Sign up For Our <b>Newsletter</b></h2>
  <div class="field">Email Address</div>
  <a class="go">SIGN UP NOW</a>
</section>

<section class="abs feature blog-intro">
  <h2>From the</h2>
  <h3>Blog posts</h3>
  <p>Lorem Ipsum is simply dummy text of the printing and typesetting industry. Lorem Ipsum has been the industry's standard dummy text ever since the 1500s</p>
  <a class="btn">EXPLORE BLOGS</a>
</section>

<div class="photo post-photo-1" role="img" aria-label="Photo of a person using a blue light whitening device"></div>
<article class="abs post" style="left:413px;top:3018px">
  <h4>Blog Post Title 01</h4>
  <time>June 27, 2019</time>
  <p style="margin-top:22px">Lorem Ipsum is simply dummy text of the printing and typesetting industry. Lorem Ipsum has been the industry's standard dummy text ever since the 1500s</p>
  <a class="more">READ MORE <svg width="13" height="13" viewBox="0 0 13 13" class="icon" style="stroke-width:1"><circle cx="6.5" cy="6.5" r="5.5"/><path d="M4 6.5h5M7 4.5l2 2-2 2"/></svg></a>
</article>

<div class="photo post-photo-2" role="img" aria-label="Photo of a hand holding a whitening pen"></div>
<article class="abs post" style="left:773px;top:2660px">
  <div style="position:absolute;left:125px;top:0;width:200px">
    <h4>Blog Post Title 02</h4>
    <time>June 27, 2019</time>
  </div>
  <p style="margin-top:137px">Lorem Ipsum is simply dummy text of the printing and typesetting industry. Lorem Ipsum has been the industry's standard dummy text ever since the 1500s</p>
  <a class="more">READ MORE <svg width="13" height="13" viewBox="0 0 13 13" class="icon" style="stroke-width:1"><circle cx="6.5" cy="6.5" r="5.5"/><path d="M4 6.5h5M7 4.5l2 2-2 2"/></svg></a>
</article>

<div class="photo post-photo-3" role="img" aria-label="Close-up photo of lips showing teeth before and after whitening"></div>
<article class="abs post" style="left:773px;top:2953px">
  <div style="position:absolute;left:125px;top:0;width:200px">
    <h4>Blog Post Title 03</h4>
    <time>June 27, 2019</time>
  </div>
  <p style="margin-top:137px">Lorem Ipsum is simply dummy text of the printing and typesetting industry. Lorem Ipsum has been the industry's standard dummy text ever since the 1500s</p>
  <a class="more">READ MORE <svg width="13" height="13" viewBox="0 0 13 13" class="icon" style="stroke-width:1"><circle cx="6.5" cy="6.5" r="5.5"/><path d="M4 6.5h5M7 4.5l2 2-2 2"/></svg></a>
</article>

<footer class="abs footer">
  <a class="abs brand" style="left:39px;top:64px">Velvet<b>Beaming</b></a>
  <ul class="fcol" style="left:39px;top:127px">
    <li>012 555 0147</li><li>012 555 0147</li><li>hello@velvetbeaming.com</li><li>2217 Linden Grove Lane</li><li>Ontario, CA 91761</li>
  </ul>
  <ul class="fcol" style="left:314px;top:127px">
    <h5>Quick Links</h5>
    <li>Home</li><li>Shop Products</li><li>Enrooled Monthly Plans</li><li>About us</li><li>Contact us</li>
  </ul>
  <ul class="fcol" style="left:548px;top:127px">
    <h5>Account</h5>
    <li>Login</li><li>Sign up</li><li>My Account</li><li>Checkout</li><li>Return Policy</li>
  </ul>
  <ul class="fcol" style="left:752px;top:127px">
    <h5>Info</h5>
    <li>Privacy Policy</li><li>Terms &amp; Condition</li><li>Customer Support</li><li>Shipping</li><li>FAQ</li>
  </ul>
  <div class="fcol" style="left:970px;top:127px">Credit Card Accepted</div>
  <div class="cards">
    <span class="card" style="background:#253b80">PayNova</span>
    <span class="card" style="background:#1a1f71">Cardia</span>
    <span class="card" style="background:#2b2b2b">Duocard</span>
    <span class="card" style="background:#2e77bc">Axiom</span>
  </div>
</footer>

<div class="abs bottom">
  <span class="copy">Copyright © 2019 Velvet Beaming. All Right Resreved</span>
  <div class="social"><span>Folio</span><span>Chirpa</span><span>Gather</span><span>Snapline</span><span>Pinboardly</span></div>
</div>

</body>
</html>
```